Business & Good Life in perfect harmony

Our company is engage in event planning & services , we have Convention center ideal for seminars, retreats,conventions, conferences or even concerts & also offers lodging facilities particularly of "ON - LINE ROOM RESERVATIONS /ACCOMMODATIONS "
Also we have Clubhouse & restobar , an elegant venue ideal for weddings, birthday celebration, parties & other memorable gatherings, as well as sports activities.
Target Market(s)
Travellers
Event Organizers
Conference / seminar Coordinators
Industry/Entity Type
Event Planning
Contact Information for Business Card
Lia R. Montero , Sales & Operation Manager
Bluecrest Business & Convention Center Corp.
/ Bluecrest Clubhouse & Restobar
Contact #s : 082-5913026 ; 0917 4356128
Website : www. bluecrestplaza.example
Email add : bluecrest.lia.plaza@mailbox.example
bluecrest.plaza@inbox.example
Facebook : Bluecrest Plaza

```html
<!DOCTYPE html>
<html lang="en">
<head>
<meta charset="utf-8">
<title>Lia R. Montero – Business Card</title>
<link href="https://fonts.googleapis.com/css2?family=Oswald:wght@400;500&family=Roboto:wght@400;500;900&display=swap" rel="stylesheet">
<style>
  :root {
    --backdrop: #2a2a2a;
    --yellow: #f2e825;
    --mint: #b9dba4;
    --ink: #111111;
    --black: #050505;
    --white: #ffffff;
    --pool: #4fb3b0;
    --sky: #9aa3ad;
  }
  * { margin: 0; padding: 0; box-sizing: border-box; }
  html, body { width: 1200px; height: 899px; overflow: hidden; background: var(--backdrop); }
  .stage { position: relative; width: 1200px; height: 899px; }
  .card {
    position: absolute; left: 100px; top: 165px; width: 1000px; height: 570px;
    background: var(--mint); overflow: hidden;
  }
  .card__top { position: absolute; left: 0; top: 0; width: 100%; height: 80px; background: var(--yellow); }
  .card__name {
    position: absolute; left: 50px; top: 12px;
    font: italic 500 44px/1 "Oswald", sans-serif; color: var(--ink); letter-spacing: 1px;
  }
  .card__tab { position: absolute; right: 0; top: 40px; width: 470px; height: 56px; }
  .card__title {
    position: absolute; right: 30px; top: 60px;
    font: italic 400 20px/1 "Oswald", sans-serif; color: var(--white); letter-spacing: 0.5px;
  }
  .card__company {
    position: absolute; left: 40px; top: 104px;
    font: 900 25px/1 "Roboto", sans-serif; color: var(--ink); letter-spacing: 1.5px; white-space: nowrap;
  }
  .card__service {
    position: absolute; right: 60px; top: 150px;
    font: 500 20px/1 "Roboto", sans-serif; color: var(--ink); letter-spacing: 2px;
  }
  .card__photo {
    position: absolute; left: 24px; top: 140px; width: 380px; height: 330px;
    background: linear-gradient(180deg, var(--sky) 0%, #c9ced2 30%, #7d8a6f 55%, var(--pool) 72%, #9a9a92 100%);
  }
  .contacts { position: absolute; left: 440px; top: 222px; list-style: none; }
  .contacts li {
    display: flex; align-items: center; gap: 14px; height: 32px;
    font: 500 20px/1 "Roboto", sans-serif; color: var(--ink); letter-spacing: 1.6px; white-space: nowrap;
  }
  .contacts .gap { margin-top: 14px; }
  .icon { width: 20px; height: 20px; flex: none; }
  .icon--dot { width: 16px; height: 16px; border-radius: 50%; background: var(--ink); margin: 0 2px; }
  .card__stripe { position: absolute; left: 0; top: 478px; width: 100%; height: 22px; background: var(--yellow); }
  .card__base { position: absolute; left: 0; top: 500px; width: 100%; height: 70px; background: var(--black); }
</style>
</head>
<body>
<main class="stage">
  <section class="card" aria-label="Business card">
    <div class="card__top"></div>
    <h1 class="card__name">Lia R. Montero</h1>
    <svg class="card__tab" viewBox="0 0 470 56" aria-hidden="true">
      <path d="M0 56 C40 56 40 14 90 14 L470 14 L470 56 Z" fill="var(--black)"/>
    </svg>
    <p class="card__title">Sales &amp; Operation Manager</p>
    <p class="card__company">BLUECREST BUSINESS &amp; CONVENTION CENTER CORP</p>
    <p class="card__service">ON - LINE ROOM RESERVATIONS</p>
    <div class="card__photo" role="img" aria-label="Photo of the clubhouse building beside its swimming pool"></div>
    <ul class="contacts">
      <li><svg class="icon" viewBox="0 0 20 20" aria-hidden="true"><rect x="1" y="4" width="18" height="13" fill="var(--ink)"/><path d="M2 5 L10 11 L18 5" stroke="var(--mint)" stroke-width="1.6" fill="none"/></svg>bluecrest.lia.plaza@mailbox.example</li>
      <li><svg class="icon" viewBox="0 0 20 20" aria-hidden="true"><rect x="1" y="4" width="18" height="13" fill="var(--ink)"/><path d="M2 5 L10 11 L18 5" stroke="var(--mint)" stroke-width="1.6" fill="none"/></svg>bluecrest.plaza@inbox.example</li>
      <li class="gap"><svg class="icon" viewBox="0 0 20 20" aria-hidden="true"><path d="M2 7 C2 3 18 3 18 7 L15 9 L13 7 L7 7 L5 9 Z" fill="var(--ink)"/><rect x="4" y="10" width="12" height="7" rx="1" fill="var(--ink)"/></svg>082-5913026</li>
      <li><svg class="icon" viewBox="0 0 20 20" aria-hidden="true"><rect x="5" y="1" width="10" height="18" rx="2" fill="none" stroke="var(--ink)" stroke-width="1.8"/><circle cx="10" cy="16" r="1" fill="var(--ink)"/></svg>0917 4356128</li>
      <li class="gap"><span class="icon icon--dot" aria-hidden="true"></span>Bluecrest Plaza</li>
      <li><svg class="icon" viewBox="0 0 20 20" aria-hidden="true"><g fill="none" stroke="var(--ink)" stroke-width="1.4"><circle cx="10" cy="10" r="8"/><ellipse cx="10" cy="10" rx="3.5" ry="8"/><path d="M2 10 H18 M3.5 6 H16.5 M3.5 14 H16.5"/></g></svg>www. bluecrestplaza.example</li>
    </ul>
    <div class="card__stripe"></div>
    <div class="card__base"></div>
  </section>
</main>
</body>
</html>
```